Letterhead Design Project

Letter head to include new logo and the following services:<br/><br/>Static Security, Mobile Patrols, Alarm Response & Key Holding, Alarm & CCTV Monitoring, Welfare Hire.<br/><br/>Phone: 0800 412 3968<br/>E-mail: security@corvane-holdings.example<br/><br/>Southern Office:<br/>Corvane Security & Monitoring<br/>2nd Floor<br/>7 Pellingham Close<br/>London<br/>N9 4HX<br/><br/>Northern Office:<br/>Corvane Security & Monitoring<br/>Crossway Nine Lorry Park<br/>Thornbury Lane<br/>Welby<br/>Sheffield<br/>S31 7QF<br/><br/>I need the files as PDF and an editable Microsoft Word Document. See attached file from my other business as an example. Do not copy information from uploaded word document, its just an example only. Logo also attached.<br/><br/><br/>SEE OTHER PROJECTS, THEY ARE ALL LINKED<br/> <br/>

```html
<!DOCTYPE html>
<html lang="en">
<head>
<meta charset="utf-8">
<title>Corvane Security &amp; Monitoring – Letterhead</title>
<link rel="stylesheet" href="https://fonts.googleapis.com/css2?family=Source+Sans+3:wght@400;600;700&family=Arimo:wght@400;700&display=swap">
<style>
  :root {
    --brand-blue: #0a6fbd;
    --brand-dark: #262729;
    --ink: #3a3a3a;
    --ink-strong: #1a1a1a;
    --paper: #ffffff;
    --backdrop: #e9e9e9;
    --footer-text: #f2f2f2;
  }
  * { box-sizing: border-box; margin: 0; padding: 0; }
  html, body { width: 1200px; height: 1200px; overflow: hidden; background: var(--backdrop); }
  .sheet-frame { position: absolute; left: 189px; top: 20px; width: 924px; height: 1304px; transform: scale(0.89); transform-origin: 0 0; }
  .sheet { position: relative; width: 924px; height: 1304px; background: var(--paper); box-shadow: 0 10px 30px rgba(0,0,0,.18); overflow: hidden; font-family: "Source Sans 3", "Myriad Pro", sans-serif; color: var(--ink); }

  .header-band { position: absolute; left: 0; top: 0; width: 924px; height: 16px; background: var(--brand-blue); }
  .header-rule { position: absolute; left: 0; top: 16px; width: 924px; height: 5px; background: var(--brand-dark); }
  .header-divider { position: absolute; left: 93px; top: 246px; width: 737px; height: 2px; background: var(--brand-blue); }

  .brand { position: absolute; left: 85px; top: 70px; display: flex; align-items: center; gap: 14px; }
  .brand-dot { width: 58px; height: 58px; border-radius: 50%; background: var(--brand-blue); flex: none; }
  .brand-name { font-size: 28px; font-weight: 600; line-height: 1.05; color: var(--brand-blue); }

  .services { position: absolute; left: 619px; top: 116px; height: 102px; border-left: 2px solid var(--brand-dark); padding-left: 12px; list-style: none; }
  .services li { display: flex; align-items: center; height: 21.4px; font-size: 14.5px; color: var(--ink-strong); }
  .services svg { width: 15px; height: 15px; margin-right: 8px; flex: none; }

  .salutation { position: absolute; left: 93px; top: 305px; font-family: "Arimo", Arial, sans-serif; font-weight: 700; font-size: 20px; color: var(--ink-strong); }
  .letter-body { position: absolute; left: 93px; top: 357px; width: 737px; }
  .letter-body p { font-size: 19.6px; line-height: 24.3px; text-align: justify; margin-bottom: 24.3px; }

  .sign-off { position: absolute; left: 105px; top: 920px; font-family: "Arimo", Arial, sans-serif; font-size: 17px; color: var(--ink-strong); }
  .signature { position: absolute; left: 102px; top: 946px; width: 136px; height: 48px; background: linear-gradient(90deg, rgba(30,30,30,.18), rgba(30,30,30,.05)); border-radius: 4px; }
  .signer { position: absolute; left: 105px; top: 997px; font-family: "Arimo", Arial, sans-serif; font-weight: 700; font-size: 17px; color: var(--ink-strong); }

  .footer-rule { position: absolute; left: 0; top: 1214px; width: 924px; height: 3px; background: var(--brand-blue); }
  .footer-band { position: absolute; left: 0; top: 1221px; width: 924px; height: 83px; background: var(--brand-dark); }
  .footer { position: absolute; left: 95px; top: 1232px; color: var(--footer-text); font-size: 14px; line-height: 21.5px; }
  .footer-contact { display: flex; align-items: center; font-size: 15px; }
  .footer-contact svg { width: 13px; height: 11px; margin-right: 4px; }
  .footer-contact .email-icon { margin-left: 10px; }
  .footer strong { font-weight: 700; margin-right: 6px; }
</style>
</head>
<body>
  <div class="sheet-frame">
    <div class="sheet">
      <div class="header-band"></div>
      <div class="header-rule"></div>

      <div class="brand">
        <span class="brand-dot"></span>
        <div class="brand-name">Corvane Security<br>&amp; Monitoring</div>
      </div>

      <ul class="services">
        <li><svg viewBox="0 0 16 16"><circle cx="8" cy="8" r="8" fill="var(--brand-blue)"/><path d="M4.5 8.3l2.3 2.2 4.7-4.8" stroke="#fff" stroke-width="1.8" fill="none"/></svg>Static Security,</li>
        <li><svg viewBox="0 0 16 16"><circle cx="8" cy="8" r="8" fill="var(--brand-blue)"/><path d="M4.5 8.3l2.3 2.2 4.7-4.8" stroke="#fff" stroke-width="1.8" fill="none"/></svg>Mobile Patrols,</li>
        <li><svg viewBox="0 0 16 16"><circle cx="8" cy="8" r="8" fill="var(--brand-blue)"/><path d="M4.5 8.3l2.3 2.2 4.7-4.8" stroke="#fff" stroke-width="1.8" fill="none"/></svg>Alarm Response &amp; Key Holding,</li>
        <li><svg viewBox="0 0 16 16"><circle cx="8" cy="8" r="8" fill="var(--brand-blue)"/><path d="M4.5 8.3l2.3 2.2 4.7-4.8" stroke="#fff" stroke-width="1.8" fill="none"/></svg>Alarm &amp; CCTV Monitoring,</li>
        <li><svg viewBox="0 0 16 16"><circle cx="8" cy="8" r="8" fill="var(--brand-blue)"/><path d="M4.5 8.3l2.3 2.2 4.7-4.8" stroke="#fff" stroke-width="1.8" fill="none"/></svg>Welfare Hire.</li>
      </ul>

      <div class="header-divider"></div>

      <p class="salutation">Dear Mr. John,</p>

      <div class="letter-body">
        <p>Lorem Ipsum is simply dummy text of the printing and typesetting industry. Lorem Ipsum has been the industry's standard dummy text ever since the 1500s, when an unknown printer took a galley of type and scrambled it to make a type specimen book. It has survived not only five centuries, but also the leap into electronic typesetting, remaining essentially unchanged.</p>
        <p>The standard chunk of Lorem Ipsum used since the 1500s is reproduced below for those interested. Sections 1.10.32 and 1.10.33 from "de Finibus Bonorum et Malorum" by Cicero are also reproduced in their exact original form, accompanied by English versions from the 1914 translation by H. Rackham</p>
        <p>Lorem Ipsum is simply dummy text of the printing and typesetting industry. Lorem Ipsum has been the industry's standard dummy text ever since the 1500s, when an unknown printer took a galley of type and scrambled it to make a type specimen book. It has survived not only five centuries, but also the leap into electronic typesetting, remaining essentially unchanged. It was popularised in the</p>
        <p>The standard chunk of Lorem Ipsum used since the 1500s is reproduced below for those interested. Sections 1.10.32 and 1.10.33 from "de Finibus Bonorum et Malorum" by Cicero are also reproduced in their exact original form, accompanied by English versions from the 1914 translation by H. Rackham</p>
      </div>

      <p class="sign-off">Lorem Ipsum</p>
      <div class="signature" role="img" aria-label="Handwritten signature of the sender"></div>
      <p class="signer">Lorem Ipsum Admin</p>

      <div class="footer-rule"></div>
      <div class="footer-band"></div>
      <div class="footer">
        <div class="footer-contact">
          <svg viewBox="0 0 13 11"><path fill="var(--brand-blue)" d="M1 3c0-2 11-2 11 0v1.5H9.5V3.4h-6v1.1H1z M3 5h7l1.5 5h-10z"/></svg>0800 412 3968
          <svg class="email-icon" viewBox="0 0 13 11"><rect x="0.5" y="1.5" width="12" height="8" fill="var(--brand-blue)"/><path d="M0.5 1.5l6 4.5 6-4.5" stroke="#fff" fill="none"/></svg>security@corvane-holdings.example
        </div>
        <div><strong>Northern Office:-</strong>Crossway Nine Lorry Park, Thornbury Lane, Welby, Sheffield, S31 7QF</div>
        <div><strong>Southern Office:-</strong>2nd Floor, 7 Pellingham Close, London, N9 4HX</div>
      </div>
    </div>
  </div>
</body>
</html>
```